Lantern over the Harbor ~ A Widening Passage for Writers

My book is called “Lantern over the Harbor.” Its subtitle is “A Widening Passage for Writers.” It is a book about being a poet, writing poetry, and the ways in which poets are connected to both society and the central energy of the Universe. I want the cover design to be abstract and impressionistic. A suggestion of fireworks or a starburst would be a plus. To be consistent with the 3 other books I have published, I want the font for the title, as well as my name (Dorothea Quillbrake) to be Papyrus. The subtitle font can be something more plain and sans serif, like Arial or Franklin Gothic Book, probably in italics. As for color, I definitely want pale gold (angelic). Possible other complimentary colors could be either light or dark shades of gray, turquoise, rose, rust or red. I'm attaching the back cover text and also three pages from inside the book that have line drawings, to give an example of the interior artwork.
Updates

Forgot to mention: My book is a paperback. Its size will be 8.5" high and 5.5" wide. I'm self-publishing it, and it will be printed by Halvern Printworks in Nebraska, USA. It has 104 pages. I think you need the number of pages, in order to make the spine of the book the correct width.

Target Market(s)

My target market is people who write poetry or are interested in how poetry is written.

Industry/Entity Type

Poetry

Font styles to use
Sans Serif
Other font styles liked:
• Papyrus for the front cover. Arial or another sans serif font on the back cover.

Colors

Designer to choose colors to be used in the design.

Requirements
Must have
• My book cover needs to be inspiring and uplifting, as well as abstract and impressionistic, with kind of a "New Age" feel. I don't want anything that looks rigid and scholarly.
Nice to have
• The book talks about the connection poets have to the Universe and the Creative Energy at the center of everything. The cover should convey that Energy.
Should not have
• My cover should not be realistic, logical or straight-laced. I want something that feels free, imaginative and unfettered.

```html
<!DOCTYPE html>
<html lang="en">
<head>
<meta charset="utf-8">
<title>Lantern over the Harbor — Cover Wrap</title>
<link rel="stylesheet" href="https://fonts.googleapis.com/css2?family=Macondo&family=Arimo:ital,wght@0,400;0,700;1,700&family=Roboto+Condensed&family=Open+Sans:ital@1&display=swap">
<style>
  :root {
    --page: #ffffff;
    --umber-dark: #2a1b10;
    --umber: #4a3220;
    --rust: #7a4a22;
    --moss: #3d3a26;
    --ink-light: #f4efe6;
    --gold: #f2c66a;
    --rose: #d8563a;
    --turquoise: #3fa3a3;
  }
  * { margin: 0; padding: 0; box-sizing: border-box; }
  html, body { width: 1200px; height: 1200px; overflow: hidden; background: var(--page); }
  .wrap {
    position: absolute; left: 67px; top: 219px; width: 1066px; height: 761px;
    display: flex; color: var(--ink-light);
  }
  .back-cover {
    width: 508px; height: 100%; position: relative;
    background:
      radial-gradient(ellipse at 20% 15%, rgba(122,74,34,.55), transparent 55%),
      radial-gradient(ellipse at 80% 85%, rgba(110,70,30,.5), transparent 60%),
      radial-gradient(ellipse at 60% 40%, rgba(61,58,38,.6), transparent 50%),
      linear-gradient(160deg, var(--umber) 0%, var(--umber-dark) 50%, #3a2616 100%);
    padding: 30px 27px 0;
  }
  .spine {
    width: 50px; height: 100%;
    background: linear-gradient(180deg, #4a3018, var(--rust) 40%, #3b2614 100%);
    display: flex; align-items: center; justify-content: center;
  }
  .spine-text {
    writing-mode: vertical-rl;
    font-family: "Macondo", fantasy;
    font-size: 32px; white-space: nowrap;
    display: flex; justify-content: space-between; height: 700px;
  }
  .front-cover {
    width: 508px; height: 100%; position: relative; overflow: hidden;
    background:
      radial-gradient(ellipse at 50% 58%, rgba(63,163,163,.35), transparent 55%),
      radial-gradient(ellipse at 85% 25%, rgba(160,90,30,.55), transparent 50%),
      radial-gradient(ellipse at 15% 70%, rgba(60,70,40,.6), transparent 50%),
      linear-gradient(170deg, #3b2b1a, #2e2a1c 50%, #3a2414);
  }
  .back-title, .front-title {
    font-family: "Macondo", fantasy; text-align: center; line-height: .95;
  }
  .back-title .big { font-size: 46px; display: block; }
  .back-title .small { font-size: 26px; display: block; }
  .chapter-list {
    font-family: "Roboto Condensed", sans-serif; font-size: 19px;
    text-align: center; line-height: 28px; margin-top: 14px;
  }
  .blurb {
    font-family: "Arimo", sans-serif; font-size: 10.2px; line-height: 17.5px;
    text-align: justify; margin-top: 12px;
  }
  .blurb p + p { margin-top: 17px; }
  .author-bio { display: flex; gap: 14px; margin-top: 20px; }
  .author-photo {
    flex: 0 0 81px; height: 110px; margin-left: 6px;
    background: linear-gradient(160deg, #b9b3ab, #c99a86 55%, #6f8f6a);
  }
  .author-bio p { font-family: "Arimo", sans-serif; font-size: 10.2px; line-height: 17.6px; text-align: justify; }
  .front-title { padding-top: 28px; }
  .front-title .line-1 { font-size: 98px; display: block; }
  .front-title .line-2 { font-size: 48px; display: block; margin-top: -4px; }
  .front-title .line-3 { font-size: 84px; display: block; margin-top: -6px; }
  .subtitle {
    font-family: "Open Sans", sans-serif; font-style: italic;
    font-size: 25px; text-align: center; margin-top: 14px; letter-spacing: .5px;
  }
  .cover-art {
    position: absolute; left: 64px; top: 296px; width: 380px; height: 390px;
    background:
      radial-gradient(circle at 50% 45%, rgba(255,240,190,.95) 0%, rgba(242,198,106,.8) 18%, rgba(216,86,58,.65) 38%, rgba(63,163,163,.45) 60%, transparent 75%);
    border-radius: 50%;
  }
  .front-author {
    position: absolute; left: 0; right: 0; top: 682px;
    font-family: "Macondo", fantasy; font-size: 44px; text-align: center;
  }
</style>
</head>
<body>
<div class="wrap">
  <section class="back-cover">
    <h2 class="back-title"><span class="big">Lantern</span><span class="small">over the</span><span class="big">Harbor</span></h2>
    <div class="chapter-list">
      The seven intriguing chapters in Lantern over the Harbor are<br>
      LIBERATION ~ EXPERIENCE ~ WORDS ~ POETRY ~<br>
      INTEGRITY ~ BEAUTY ~ CREATION
    </div>
    <div class="blurb">
      <p><b><i>Lantern over the Harbor</i></b> is indeed “A Widening Passage for Writers.” It is written by Dorothea Quillbrake, an exciting, imaginative voice in American poetry.</p>
      <p>In <b><i>Lantern over the Harbor,</i></b> Dorothea discusses the essential elements of poetry and the process of writing it. She offers an inspiring view of the mission of poets and their connection to both society and the larger forces in the Universe. Her book is motivational, refreshing and irrepressibly optimistic.</p>
    </div>
    <div class="author-bio">
      <div class="author-photo" role="img" aria-label="Portrait photograph of the author"></div>
      <p>For over 50 years, Dorothea has been a teacher of writing and poetry. Since 2007, she has published three books of her poems: <b><i>Mind the Garden Gate, The Silver Edge of Evening</i></b> and <b><i>The Quiet Velvet Sky.</i></b> Her work overflows with her characteristically rich images and quirky metaphors. It runs the gamut from subtle eroticism to abject grief, from defiant rage to philosophical meditation, and from borderline blasphemy to lyrical fantasy.</p>
    </div>
    <p class="blurb" style="margin-top:0">Dorothea has been called by critic Gareth Wenlow “a poet to be reckoned with; bright, feisty, compassionate.” (The Riverside Ledger, Maplebrook, OR). Author Lorna Ashdell (“Thistlegate,” 2011) says Dorothea’s poetry is like “a perpetual Surprise Party ~ memorable, insightful and thematically fascinating.</p>
  </section>
  <div class="spine">
    <div class="spine-text"><span>Lantern over the Harbor</span><span>Dorothea Quillbrake</span></div>
  </div>
  <section class="front-cover">
    <h1 class="front-title"><span class="line-1">Lantern</span><span class="line-2">over the</span><span class="line-3">Harbor</span></h1>
    <p class="subtitle">A Widening Passage for Writers</p>
    <div class="cover-art" role="img" aria-label="Abstract radiant winged figure bursting in gold, red and turquoise light"></div>
    <p class="front-author">Dorothea Quillbrake</p>
  </section>
</div>
</body>
</html>
```